professional business card design for technology company

We are a small technology consulting firm, specialising in consulting based around Cloud and Managed services. Our colour scheme is yellow, blue and white, as you can see in the logos. Although we are based in melbourne australia, due to the nature of our work, our clients can be located anywhere. We are looking for a clean, professional, positive look - similar to our company logo

Target Market(s)

small business

Industry/Entity Type

Business

Contact Information for Business Card

eye catching, designed to incorporate some level of raised printing. Must contain website address, phone number, name and job title

Requirements
Must have
• Logo (attached) - use of the same colour scheme

```html
<!DOCTYPE html>
<html lang="en">
<head>
<meta charset="UTF-8">
<title>Nimbora – Business Card</title>
<link href="https://fonts.googleapis.com/css2?family=Raleway:wght@400;500;700&family=Montserrat:wght@700;800&display=swap" rel="stylesheet">
<style>
  :root{
    --bg:#e6e4e1;
    --paper:#f1f1f1;
    --ink:#2d2d2d;
    --brand-grey:#555658;
    --blue:#2aa6e0;
    --yellow:#f4cf0c;
    --light:#f2f2f2;
    --muted:#c9c9c9;
  }
  *{margin:0;padding:0;box-sizing:border-box}
  html,body{width:1200px;height:960px;overflow:hidden;background:var(--bg)}
  .canvas{position:relative;width:1200px;height:960px;font-family:'Raleway',sans-serif}

  .card{position:absolute;left:250px;width:700px;height:400px;background:var(--paper);overflow:hidden;box-shadow:0 10px 28px rgba(0,0,0,.18)}
  .card--front{top:50px}
  .card--back{top:510px}

  .wordmark{display:flex;align-items:center;gap:16px}
  .wordmark__dot{width:22px;height:22px;border-radius:50%;background:var(--blue)}
  .wordmark__name{font-family:'Montserrat',sans-serif;font-weight:800;color:var(--brand-grey);letter-spacing:-1px}

  .card--front .wordmark{position:absolute;left:0;right:0;top:120px;justify-content:center}
  .card--front .wordmark__name{font-size:64px}

  .front-band{position:absolute;left:0;right:0;bottom:0;height:86px;background:var(--ink);border-top:6px solid var(--yellow);display:flex;align-items:center;justify-content:center;gap:12px}
  .front-band__url{color:var(--light);font-size:17px;letter-spacing:2px}

  .icon{width:14px;height:14px;flex:none}

  .back-yellow{position:absolute;inset:0;background:var(--yellow);clip-path:polygon(62.2% 0,100% 0,100% 100%,53.2% 100%)}
  .back-panel{position:absolute;inset:0;background:var(--ink);clip-path:polygon(63.4% 0,100% 0,100% 100%,54.4% 100%)}

  .card--back .wordmark{position:absolute;left:40px;top:0;bottom:0;width:300px;flex-direction:column;justify-content:center;gap:14px}
  .card--back .wordmark__dot{width:34px;height:34px}
  .card--back .wordmark__name{font-size:56px}

  .contact{position:absolute;left:440px;top:100px;width:240px;color:var(--light)}
  .contact__person{display:flex;align-items:center;gap:12px;margin-bottom:34px}
  .ring{width:36px;height:36px;border:2px solid var(--blue);border-radius:50%;display:flex;align-items:center;justify-content:center;flex:none}
  .ring--small{width:30px;height:30px}
  .contact__name{font-size:20px;font-weight:400;letter-spacing:.5px}
  .contact__name .first{color:var(--blue);font-weight:700}
  .contact__role{font-size:13px;color:var(--muted);margin-top:2px}
  .contact__list{list-style:none}
  .contact__item{display:flex;align-items:center;gap:12px;font-size:14px;margin-bottom:12px}
</style>
</head>
<body>
<main class="canvas">

  <section class="card card--front">
    <div class="wordmark">
      <span class="wordmark__dot"></span>
      <span class="wordmark__name">Nimbora</span>
    </div>
    <div class="front-band">
      <svg class="icon" viewBox="0 0 16 16"><circle cx="8" cy="8" r="7" fill="var(--blue)"/><path d="M1 8h14M8 1c3 3 3 11 0 14M8 1c-3 3-3 11 0 14" stroke="var(--ink)" stroke-width="1.2" fill="none"/></svg>
      <span class="front-band__url">www.nimbora.com</span>
    </div>
  </section>

  <section class="card card--back">
    <div class="wordmark">
      <span class="wordmark__dot"></span>
      <span class="wordmark__name">Nimbora</span>
    </div>
    <div class="back-yellow"></div>
    <div class="back-panel"></div>
    <div class="contact">
      <div class="contact__person">
        <span class="ring">
          <svg class="icon" viewBox="0 0 16 16"><circle cx="8" cy="5" r="3.5" fill="var(--light)"/><path d="M1.5 15c0-4 3-6 6.5-6s6.5 2 6.5 6z" fill="var(--light)"/></svg>
        </span>
        <div>
          <div class="contact__name"><span class="first">DANIEL</span> HART</div>
          <div class="contact__role">Sales Director</div>
        </div>
      </div>
      <ul class="contact__list">
        <li class="contact__item">
          <span class="ring ring--small"><svg class="icon" viewBox="0 0 16 16"><path d="M4 1.5l2.5 3-1.5 1.8c.8 1.8 2.2 3.2 4 4l1.8-1.5 3 2.5-1.5 2.5C7 13.5 2.5 9 1.5 3z" fill="var(--light)"/></svg></span>
          555-014-2287
        </li>
        <li class="contact__item">
          <span class="ring ring--small"><svg class="icon" viewBox="0 0 16 16"><rect x="1" y="3" width="14" height="10" rx="1" fill="var(--light)"/><path d="M1.5 3.5L8 9l6.5-5.5" stroke="var(--ink)" stroke-width="1.3" fill="none"/></svg></span>
          hello@nimbora.com
        </li>
        <li class="contact__item">
          <span class="ring ring--small"><svg class="icon" viewBox="0 0 16 16"><circle cx="8" cy="8" r="7" fill="var(--light)"/><path d="M1 8h14M8 1c3 3 3 11 0 14M8 1c-3 3-3 11 0 14" stroke="var(--ink)" stroke-width="1.2" fill="none"/></svg></span>
          www.nimbora.com
        </li>
      </ul>
    </div>
  </section>

</main>
</body>
</html>
```